■依頼の概要
子どもの結婚を望む親御様に向けた電子書籍(pagora出版)の表紙デザイン作成をお願いします。
電子書籍なので、タイトルがはっきり分かるものでお願いします。

■本のタイトル
いつか、わが家にも春は来るだろうか? ~家族の未来をひらく手引き~

■本の内容
子どもの結婚を望む親御様に向けて、今どきの婚活・結婚事情をデータでご紹介している他、婚活成幸するための考え方や事例を紹介しています。
原稿内容を添付します。

■読者ターゲット
息子・娘に結婚してほしいと願っている親御様
(20代~50代位の独身のお子さんに結婚してほしいと願っている親御様・子どもの結婚のためなら何でもする覚悟の親御様・親子関係が良好ではない親御様)

■デザイン要望
原稿内容を参考にしていただいて、より売れることを目的としたデザインにしてください。
デザイナーさんのパフォーマンスを引き出したいので、デザイナーさんのセンスにお任せします。

■その他
Zuvomiの利用が不慣れなためアクション方法が分からず、対応がスマートでない場合はご指摘・ご教示いただけますと助かります。
何かご不明な点がございましたら、お気軽にご質問ください。
尚、最終的には私が籍を置く出版スクール内での投票で、一番人気のあったデザインに決めさせていただきます。

以上、何卒宜しくお願い申し上げます。
【ご提案をいただいた皆様へ】

この度はステキな表紙デザインを数多くご提案いただきまして、本当にありがとうございます。
皆様からいただきましたご提案は、私が籍を置く出版スクール内でのルールで、デザインの人気投票を行い一番得票数の多かったデザインを採用させていただきます。
それ故、締め切り後しばらくお時間をいただきますが、表紙をお願いしたい方には後日ご連絡をさせていただきます。
尚、全員の方お一人お一人にお礼のご挨拶ができませんことお許しいただき、この場でのご挨拶とさせていただきます。
この度の皆様からのご提案に心から感謝申し上げます。
ありがとうございましたm(__)m

皆様からご提案をいただきまして、私が籍を置く出版スクール内で表紙デザインの人気投票を行いました(これが、出版スクールでの標準的ルールになっています)
そうしましたところ、こちらのデザインに一番票が集まりました。
ご投票いただいた方々のコメントには、親の気持ちがそのままデザインに表されている・タイトルがスッと目に入ってきた・優しいピンクが、焦燥感を和らげてる・水引に縁起の良さを感じるなどたくさんのコメントをいただきました。

この度は、皆様からたくさんのご提案をいただきまして、本当にありがとうございましたm(__)m
素晴らしい作品に恵まれ、また私の好みをお伝えさせていただいた際には、皆様快く修正や追加提案をいただいて、また迅速にご対応いただいて、本当に有難く感謝の気持ちでいっぱいでおります。
これだけたくさんの、しかも素晴らしいご提案をいただいたら私自身もどれにしようか悩んでしまいました。
最終的には、人気投票で一番人気のデザインに決めさせていただきました。
この度のコンペにご参加の全ての皆様に心から感謝申し上げます。

```html
<!DOCTYPE html>
<html lang="ja">
<head>
<meta charset="utf-8">
<title>いつか、わが家にも春は来るだろうか? 表紙</title>
<link rel="stylesheet" href="https://fonts.googleapis.com/css2?family=Noto+Sans+JP:wght@500;700;900&family=Noto+Serif+JP:wght@700;900&display=swap">
<style>
  :root{
    --navy:#1d2f5c;
    --blue:#1f7fc0;
    --pink:#e8357e;
    --rose:#f3a6c4;
    --gold:#c9a460;
    --paper:#ffffff;
    --blush:#fdf1f5;
  }
  *{margin:0;padding:0;box-sizing:border-box}
  html,body{width:750px;height:1200px;overflow:hidden;background:var(--paper)}
  .cover{position:relative;width:750px;height:1200px;overflow:hidden;
    background:linear-gradient(180deg,#fff 0%,#fff 70%,var(--blush) 100%);
    font-family:"Noto Sans JP",sans-serif;color:var(--navy)}
  .hero-photo{position:absolute;left:0;top:0;width:750px;height:640px;
    background:
      linear-gradient(180deg,rgba(255,255,255,0) 35%,rgba(255,255,255,.85) 78%,#fff 100%),
      radial-gradient(ellipse at 15% 25%,#e88aa8 0%,rgba(232,138,168,0) 40%),
      radial-gradient(ellipse at 85% 30%,#f0a8bf 0%,rgba(240,168,191,0) 38%),
      radial-gradient(ellipse at 40% 30%,#5b6378 0%,rgba(91,99,120,0) 22%),
      radial-gradient(ellipse at 62% 35%,#f4f1ee 0%,rgba(244,241,238,0) 26%),
      linear-gradient(180deg,#6f9a58 0%,#9bbd7c 45%,#d9e6cf 100%)}
  .title{position:absolute;left:0;top:270px;width:750px;text-align:center;
    font-weight:900;line-height:1.05;letter-spacing:.02em;
    text-shadow:0 0 6px #fff,0 0 6px #fff,0 0 10px #fff,0 0 14px #fff}
  .title .line{display:block}
  .title .lead{font-size:74px;color:var(--navy)}
  .title .main{font-size:140px;margin-top:10px}
  .title .main .spring{color:var(--pink)}
  .title .main .come{color:var(--blue)}
  .title .main .particle{font-size:104px;color:var(--navy)}
  .title .tail{font-size:96px;color:var(--blue);margin-top:8px}
  .ornament-flourish{position:absolute;left:520px;top:610px;width:140px;height:90px;border-radius:45px;
    background:radial-gradient(ellipse,rgba(201,164,96,.55),rgba(201,164,96,0) 70%)}
  .subtitle{position:absolute;left:138px;top:715px;font-family:"Noto Serif JP",serif;font-weight:900;
    font-size:46px;line-height:1.35;color:var(--pink);letter-spacing:.04em}
  .ornament-corner{position:absolute;left:38px;top:830px;width:110px;height:95px;
    background:linear-gradient(135deg,rgba(201,164,96,.55),rgba(201,164,96,0) 75%)}
  .author{position:absolute;right:48px;top:858px;text-align:right}
  .author .role{font-size:28px;font-weight:700;color:var(--pink);letter-spacing:.02em}
  .author .name{font-family:"Noto Serif JP",serif;font-size:32px;font-weight:700;color:var(--navy);margin-top:4px}
  .heart{position:absolute;right:28px;top:980px;width:160px;height:120px}
  .gift{position:absolute;left:50px;top:1018px;width:662px;height:162px;border:3px solid var(--rose);
    background:rgba(255,255,255,.9)}
  .gift-tab{position:absolute;left:190px;top:-22px;padding:4px 26px;background:var(--pink);color:#fff;
    font-family:"Noto Serif JP",serif;font-weight:700;font-size:26px;letter-spacing:.08em}
  .gift-headline{position:absolute;left:0;top:34px;width:100%;text-align:center;font-family:"Noto Serif JP",serif;
    font-weight:900;font-size:40px;color:var(--pink);white-space:nowrap}
  .gift-body{position:absolute;right:24px;top:92px;width:600px;text-align:right;font-size:24px;font-weight:700;line-height:1.45;color:var(--navy);white-space:nowrap}
  .gift-body em{font-style:normal;color:var(--pink);font-size:27px}
</style>
</head>
<body>
<main class="cover">
  <div class="hero-photo" role="img" aria-label="バラの咲く庭で手をつなぐ新郎新婦の写真"></div>

  <h1 class="title">
    <span class="line lead">いつか、わが家にも</span>
    <span class="line main"><span class="spring">春</span><span class="particle">は</span><span class="come">来る</span></span>
    <span class="line tail">だろうか?</span>
  </h1>

  <div class="ornament-flourish" role="img" aria-label="金色の飾り罫"></div>

  <p class="subtitle">家族の未来を<br>ひらく手引き</p>

  <div class="ornament-corner" role="img" aria-label="金色のコーナー飾り"></div>

  <div class="author">
    <p class="role">家族の縁むすびナビゲーター</p>
    <p class="name">結 さくら 著</p>
  </div>

  <svg class="heart" viewBox="0 0 160 120" aria-hidden="true">
    <path d="M80 110 C20 70 10 40 30 20 C50 2 72 12 80 32 C88 12 110 2 130 20 C150 40 140 70 80 110 Z"
      fill="none" stroke="#f3a6c4" stroke-width="4" opacity=".7"/>
  </svg>

  <section class="gift">
    <p class="gift-tab">読者プレゼント</p>
    <p class="gift-headline">『ご縁をひらく出会い方チェック!』</p>
    <p class="gift-body">お子さんに合う出会い方が、<br>かんたんな質問で<em>すぐにわかる!</em></p>
  </section>
</main>
</body>
</html>
```